Life Saving Rules KDBRX

Design a wallet/business card size document front and back to depict the attached lifesaving rules in the color scheme of the business logo attached. (Also attached is an example of a similar card)

Target Market(s)

End User - Field Employees

Industry/Entity Type

Refining

Requirements
Must have
• All Life Saving rules with graphics, using front and back of card, information needs to flow.
Nice to have
• Would like the design to be similar to the card uploaded but better with graphics

```html
<!DOCTYPE html>
<html lang="en">
<head>
<meta charset="utf-8">
<title>Life Saving Rules – KDBRX</title>
<link rel="stylesheet" href="https://fonts.googleapis.com/css2?family=Inter:wght@300;400;700;800&display=swap">
<style>
  :root {
    --blue: #1ba1dc;
    --green: #76bc43;
    --ink: #4f4f4f;
    --muted: #8c8c8c;
    --card: #ffffff;
    --stage: #e4e4e4;
    --icon-tint: #d5eefa;
  }
  * { margin: 0; padding: 0; box-sizing: border-box; }
  html, body { width: 1200px; height: 2244px; overflow: hidden; }
  body {
    background: var(--stage);
    font-family: "Inter", Arial, sans-serif;
    position: relative;
  }
  .card {
    position: absolute;
    left: 100px;
    width: 1000px;
    height: 571px;
    background: var(--card);
    overflow: hidden;
    box-shadow: 0 18px 30px rgba(0,0,0,0.18);
  }
  .card--front { top: 511px; }
  .card--back { top: 1162px; }

  .network {
    position: absolute;
    width: 240px;
    height: 260px;
  }
  .network--green-tl { top: 0; left: 0; background: radial-gradient(circle at 0 0, rgba(118,188,67,0.45), rgba(118,188,67,0) 70%); width: 170px; height: 160px; }
  .network--blue-tl { top: 0; left: 0; background: radial-gradient(circle at 0 0, rgba(27,161,220,0.5), rgba(27,161,220,0) 72%); }
  .network--green-br { bottom: 0; right: 0; background: radial-gradient(circle at 100% 100%, rgba(118,188,67,0.55), rgba(118,188,67,0) 72%); width: 270px; height: 300px; }

  .brand {
    position: absolute;
    top: 60px;
    left: 0; right: 0;
    display: flex;
    justify-content: center;
    align-items: center;
    gap: 14px;
  }
  .brand__dot { width: 30px; height: 30px; border-radius: 50%; background: var(--green); }
  .brand__name { font-size: 40px; font-weight: 700; color: var(--ink); letter-spacing: -0.5px; }

  .title {
    position: absolute;
    top: 178px;
    left: 0; right: 0;
    text-align: center;
    font-size: 100px;
    letter-spacing: -5px;
    line-height: 1;
  }
  .title__strong { color: var(--blue); font-weight: 800; }
  .title__light { color: var(--green); font-weight: 400; }

  .rule {
    position: absolute;
    text-align: center;
    display: flex;
    flex-direction: column;
    align-items: center;
  }
  .rule__icon {
    width: 88px; height: 88px;
    border-radius: 10px;
    background: linear-gradient(135deg, var(--icon-tint), #b7e1f5);
    margin-bottom: 14px;
  }
  .rule__name { font-size: 25px; font-weight: 400; color: var(--ink); letter-spacing: -1px; margin-bottom: 8px; }
  .rule__text { font-size: 21px; font-weight: 300; color: var(--muted); letter-spacing: -0.8px; line-height: 1.1; }

  .front-row .rule { top: 303px; width: 320px; }
  .rule--bypass { left: 30px; }
  .rule--confined { left: 340px; }
  .rule--energy { left: 670px; }

  .divider { position: absolute; background: var(--green); }
  .divider--v1 { left: 374px; top: 370px; width: 2px; height: 135px; }
  .divider--v2 { left: 682px; top: 370px; width: 2px; height: 135px; }

  .back-grid .rule { width: 340px; }
  .rule--hot { left: 128px; top: 64px; }
  .rule--lifting { left: 522px; top: 68px; }
  .rule--permit { left: 128px; top: 314px; }
  .rule--fall { left: 522px; top: 314px; }
  .divider--cross-v { left: 499px; top: 97px; width: 2px; height: 380px; }
  .divider--cross-h { left: 159px; top: 285px; width: 682px; height: 2px; }
</style>
</head>
<body>

<section class="card card--front" aria-label="Life Saving Rules card, front">
  <div class="network network--green-tl" role="img" aria-label="Faint green network-node decoration"></div>

  <div class="brand">
    <span class="brand__dot"></span>
    <span class="brand__name">KDBRX</span>
  </div>

  <h1 class="title"><span class="title__strong">LIFE SAVING</span> <span class="title__light">RULES</span></h1>

  <div class="front-row">
    <div class="rule rule--bypass">
      <div class="rule__icon" role="img" aria-label="Line icon of a shield with a person and circuit nodes"></div>
      <h2 class="rule__name">Bypassing Safety Controls</h2>
      <p class="rule__text">Obtain authorisation before<br>overriding or disabling<br>safety controls</p>
    </div>
    <div class="rule rule--confined">
      <div class="rule__icon" role="img" aria-label="Line icon of a worker entering a confined space"></div>
      <h2 class="rule__name">Confined Space</h2>
      <p class="rule__text">Obtain authorisation before<br>entering a confined space</p>
    </div>
    <div class="rule rule--energy">
      <div class="rule__icon" role="img" aria-label="Line icon of a lightning bolt over a lock"></div>
      <h2 class="rule__name">Energy Isolation</h2>
      <p class="rule__text">Verify isolation and zero<br>energy before work begins</p>
    </div>
  </div>
  <span class="divider divider--v1"></span>
  <span class="divider divider--v2"></span>
</section>

<section class="card card--back" aria-label="Life Saving Rules card, back">
  <div class="network network--blue-tl" role="img" aria-label="Blue network-node decoration"></div>
  <div class="network network--green-br" role="img" aria-label="Green network-node decoration"></div>

  <div class="back-grid">
    <div class="rule rule--hot">
      <div class="rule__icon" role="img" aria-label="Line icon of a flame"></div>
      <h2 class="rule__name">Hot Work</h2>
      <p class="rule__text">Control flammables<br>and ignition sources</p>
    </div>
    <div class="rule rule--lifting">
      <div class="rule__icon" role="img" aria-label="Line icon of a tower crane"></div>
      <h2 class="rule__name">Safe Mechanical Lifting</h2>
      <p class="rule__text">Plan lifting operations and<br>control the area</p>
    </div>
    <div class="rule rule--permit">
      <div class="rule__icon" role="img" aria-label="Line icon of a permit checklist"></div>
      <h2 class="rule__name">Work Authorisation</h2>
      <p class="rule__text">Work with a valid<br>permit when required</p>
    </div>
    <div class="rule rule--fall">
      <div class="rule__icon" role="img" aria-label="Line icon of a person slipping and falling"></div>
      <h2 class="rule__name">Fall Protection</h2>
      <p class="rule__text">Protect yourself against a fall<br>when working at height</p>
    </div>
  </div>
  <span class="divider divider--cross-v"></span>
  <span class="divider divider--cross-h"></span>
</section>

</body>
</html>
```